Figure for Manufacture of Wound Healing Gel

Who we are: We are a nationally funded bioengineering laboratory at Harlow Ridge University conducting research on the tendon healing properties of a gel manufactured from real tendon.

What we need: We require a figure piece that will be included in an academic publication. With that in mind, the figure must be professional, clear, and concise. A reader would need to glance at the figure for only a moment to understand the process of how we manufacture and store tendon gel. Actual pictures of the in-between steps are included and will need to be cropped to improve the professional look of the design.

The Details: The figure should stepwise show the process of how we manufacture and store tendon gel. In brief, we harvest tendon from donor cadavers. Those tendons undergo decellularization, lyophilization (fancy word for freeze-drying), and are milled into a fine powder. The powder is set in acidified water and treated with digestive enzymes. After 24 hrs, the gel is brought to physiologic pH and salinity and placed in vials. The vials are frozen and again lyophilized (this is so they can be stored and transported easily). Finally the samples are reconstituted with DI water.

The Figure: Should be a linear process (horizontal). The following are the actual steps we wish to include (steps need not be numbered necessarily as long as they are in logical order...

1.) A picture of harvested tendon (Step 1.jpg)
2.) Written description: "Decellularization, lyophilization, and milling"
3.) A picture of milled tendon powder (Step 2.jpg)
4.) Written description: "Digestion with pepsin before establishing physiologic pH and salinity".
5.) A picture of gel (Step 3.jpg)
6.) Written description: "Lyophilization of aliquots"
7.) A picture of freeze-dried gel (Step 4.jpg)
8.) Written description: "Reconstitution with DI water"
9.) A picture of reconstituted gel (Step 5.jpg)

Feel free to message for any questions, comments, or clarifications.

```html
<!DOCTYPE html>
<html lang="en">
<head>
<meta charset="utf-8">
<title>Tendon Healing – Gel Manufacture Process</title>
<link href="https://fonts.googleapis.com/css2?family=Arimo:wght@400;700&display=swap" rel="stylesheet">
<style>
  :root {
    --brand-orange: #ee4419;
    --connector: #3a3a3a;
    --paper: #ffffff;
    --ink-light: #ffffff;
    --photo-tendon-a: #e9e4d6;
    --photo-tendon-b: #c9c3b3;
    --photo-powder-a: #f3efd8;
    --photo-powder-b: #cfd0cc;
    --photo-gel-a: #eef0ef;
    --photo-gel-b: #b9bcbd;
    --photo-vial-a: #ffffff;
    --photo-vial-b: #e8e2c8;
  }
  * { box-sizing: border-box; margin: 0; padding: 0; }
  html, body { width: 1200px; height: 432px; overflow: hidden; background: var(--paper); }
  body { font-family: "Arimo", Arial, sans-serif; position: relative; }

  .figure-frame {
    position: absolute; left: 40px; top: 30px; width: 1118px; height: 348px;
    border: 2px solid var(--brand-orange);
  }
  .title-band { position: absolute; left: 40px; top: 30px; width: 520px; height: 40px; }
  .title-text { position: absolute; left: 54px; top: 34px; color: var(--ink-light); }
  .title-text h1 { font-size: 19px; font-weight: 700; line-height: 20px; }
  .title-text p { font-size: 14px; line-height: 16px; }

  .step-card {
    position: absolute; top: 122px; width: 196px; height: 162px;
    border: 1.5px solid var(--brand-orange); background: var(--paper);
  }
  .step-head {
    background: var(--brand-orange); color: var(--ink-light);
    height: 46px; padding: 7px 8px 0;
  }
  .step-head h2 { font-size: 10.5px; font-weight: 700; line-height: 13px; }
  .step-head p { font-size: 8px; line-height: 9.5px; margin-top: 1px; }
  .step-photo { position: absolute; left: 2px; right: 2px; top: 48px; bottom: 2px; }
  .photo-tendon { background: radial-gradient(ellipse at center, var(--photo-tendon-a), var(--photo-tendon-b) 70%, var(--paper)); }
  .photo-powder { background: radial-gradient(ellipse at center, var(--photo-powder-a), var(--photo-powder-b) 70%, var(--paper)); }
  .photo-gel { background: radial-gradient(ellipse at center, var(--photo-gel-a), var(--photo-gel-b) 70%, var(--paper)); }
  .photo-vial { background: linear-gradient(90deg, var(--photo-vial-a), var(--photo-vial-b) 50%, var(--photo-vial-a)); }

  .connectors { position: absolute; left: 0; top: 0; }

  .caption-band {
    position: absolute; left: 40px; top: 326px; width: 1118px; height: 52px;
    background: var(--brand-orange); color: var(--ink-light);
    font-size: 10.5px; line-height: 14px; padding: 6px 12px 0 12px;
  }
</style>
</head>
<body>
  <div class="figure-frame"></div>
  <svg class="title-band" width="520" height="40" viewBox="0 0 520 40" aria-hidden="true">
    <polygon points="0,0 520,0 480,40 0,40" fill="var(--brand-orange)"/>
  </svg>
  <div class="title-text">
    <h1>Tendon Healing</h1>
    <p>Gel Manufactured From Real Tendon.</p>
  </div>

  <svg class="connectors" width="1200" height="432" viewBox="0 0 1200 432" aria-hidden="true">
    <g fill="none" stroke="var(--connector)" stroke-width="1.5">
      <polyline points="392,117 392,104 597,104 597,117"/>
      <polyline points="806,117 806,104 1010,104 1010,117"/>
      <polyline points="181,288 181,297 391,297 391,288"/>
      <polyline points="598,288 598,297 806,297 806,288"/>
    </g>
  </svg>

  <section class="step-card" style="left:92px">
    <div class="step-head"><h2>Picture Of Harvested Tendon</h2><p>Decellularization, lyophilization, and milling</p></div>
    <div class="step-photo photo-tendon" role="img" aria-label="Photo of harvested tendon strands in a glass dish"></div>
  </section>
  <section class="step-card" style="left:298px">
    <div class="step-head"><h2>A Picture Of Milled Tendon Powder</h2><p>Digestion with pepsin before establishing physiologic pH and salinity</p></div>
    <div class="step-photo photo-powder" role="img" aria-label="Photo of milled tendon powder in a glass dish"></div>
  </section>
  <section class="step-card" style="left:504px">
    <div class="step-head"><h2>A Picture Of Gel</h2><p>Lyophilization of aliquots</p></div>
    <div class="step-photo photo-gel" role="img" aria-label="Photo of tendon gel in a glass dish"></div>
  </section>
  <section class="step-card" style="left:710px">
    <div class="step-head"><h2>A picture of freeze-dried gel</h2><p>Reconstitution with DI water</p></div>
    <div class="step-photo photo-vial" role="img" aria-label="Photo of freeze-dried gel in a capped vial"></div>
  </section>
  <section class="step-card" style="left:914px">
    <div class="step-head"><h2>A picture of reconstituted gel</h2></div>
    <div class="step-photo photo-vial" role="img" aria-label="Photo of reconstituted gel in a capped vial"></div>
  </section>

  <div class="caption-band">
    Those tendons undergo decellularization, lyophilization (fancy word for freeze-drying), and are milled into a fine powder. The powder is set in acidified water and treated with digestive enzymes. After 24 hrs, the gel is brought to physiologic pH and salinity and placed in vials. The vials are frozen and again lyophilized (this is so they can be stored and transported easily). Finally the samples are reconstituted with DI water.
  </div>
</body>
</html>
```